KLT-AZ Presentation Folder

The old design is attached. We're looking to revamp our Arizona offices with a fresh new look.

Front Cover

The Company Logo is prominently displayed.
Tagline: "Improving Homes. Improving Lives."
Image of a beautiful home showcasing new windows and doors
Website: crestfieldpaneworksaz.example
Social media icons: Chatterloop, Snapvale, ClipDrome, Rateburrow
Mention: "Follow us for the latest updates and tips."

Back Cover

Thank You Message: "Thank you for choosing Crestfield Pane Works. We appreciate your trust in us to improve your home."
Contact Information:
Customer Service: 480.555.0187
Call Center: 480.555.0143
ROC License Number: #418302
Additional social media handles and website details.
Small disclaimer or legal note if necessary.

Inside Left Panel

Photo of Doug and Marian Solvik (founders)
Short blurb/quote: “Our mission is to provide the best window and door solutions with a personal touch. Thank you for letting us be a part of your home improvement journey.”
Slots for business cards (either sales or customer service rep)

Inside Right Panel

Thank You Message: “We’re honored to be a part of your home transformation. Our commitment to quality and customer satisfaction ensures you receive the best service and products.”
List of Services (e.g., window and door installations, energy-efficient solutions)
Highlight the company’s QTC accreditation A+

Encourage the customer to reach out if they need further assistance or have any questions, with a reminder of the contact details.

https://www.qtcreview.example/us/az/gilbert/profile/home-improvement/crestfield-pane-works-4471-2000058314

https://crestfieldpaneworksaz.example/

We need thirty more days to decide.

Gathering more feedback

Designs look the same

```html
<!DOCTYPE html>
<html lang="en">
<head>
<meta charset="utf-8">
<title>Crestfield Pane Works Presentation Folder</title>
<link rel="stylesheet" href="https://fonts.googleapis.com/css2?family=Red+Hat+Display:ital,wght@0,400;0,500;0,700;1,400&family=Crimson+Pro:wght@600&display=swap">
<style>
  :root {
    --navy: #13213b;
    --navy-soft: rgba(27, 42, 72, 0.78);
    --white: #ffffff;
    --page-bg: #000000;
    --brand-blue: #2f4f86;
    --rule: #c9d1de;
    --sky: #7fa9d8;
    --floor: #5a3a25;
  }
  * { box-sizing: border-box; margin: 0; padding: 0; }
  html, body { width: 671px; height: 1200px; overflow: hidden; background: var(--page-bg); }
  body { position: relative; font-family: "Red Hat Display", Arial, sans-serif; color: var(--white); }

  .spread { position: absolute; left: 25px; width: 620px; height: 401px; overflow: hidden; }
  .spread--outside { top: 184px; }
  .spread--inside { top: 615px; background: var(--white); }

  /* Outside */
  .hero-photo {
    position: absolute; left: 0; top: 0; width: 620px; height: 346px;
    background:
      linear-gradient(180deg, rgba(50,40,35,0.9) 0%, rgba(60,50,45,0.2) 16%, rgba(0,0,0,0) 30%),
      linear-gradient(180deg, #d8d2ca 0%, var(--sky) 28%, #9fb0b6 48%, #6d8da6 60%, #7a5b45 78%, var(--floor) 100%);
  }
  .logo-corner {
    position: absolute; right: 0; top: 0; width: 132px; height: 66px;
    background: var(--white); border-bottom-left-radius: 66px;
    display: flex; align-items: center; justify-content: flex-end; padding-right: 10px; gap: 4px;
  }
  .logo-mark { width: 12px; height: 12px; background: var(--brand-blue); flex: none; }
  .logo-name { font-weight: 700; font-size: 9px; line-height: 1.05; color: var(--brand-blue); width: 62px; }
  .tagline {
    position: absolute; left: 333px; top: 268px;
    font-weight: 500; font-size: 29px; line-height: 35px; color: var(--white); letter-spacing: -0.2px;
  }
  .thanks-box {
    position: absolute; left: 31px; top: 297px; width: 250px; height: 38px;
    background: var(--navy-soft); padding: 7px 8px; font-size: 9.4px; line-height: 12.5px;
  }
  .outside-band { position: absolute; left: 0; top: 346px; width: 620px; height: 55px; background: var(--navy); }
  .contact { position: absolute; left: 29px; top: 5px; font-size: 5.6px; line-height: 9.4px; }
  .contact__title { font-weight: 700; border-bottom: 0.6px solid var(--rule); width: 92px; margin-bottom: 1px; }
  .contact strong { font-size: 7px; }
  .web { position: absolute; top: 10px; font-size: 5.8px; line-height: 12px; }
  .web--a { left: 175px; }
  .web--b { left: 334px; }
  .social { display: flex; gap: 3px; font-size: 4.3px; line-height: 8px; }
  .social span { display: flex; align-items: center; gap: 1.5px; }
  .social span::before { content: ""; width: 5px; height: 5px; border: 0.6px solid var(--white); border-radius: 50%; }

  /* Inside */
  .inside-band { position: absolute; left: 0; top: 277px; width: 620px; height: 124px; background: var(--navy); }
  .pocket-notch { position: absolute; left: 297px; top: 277px; }
  .founders-photo {
    position: absolute; left: 26px; top: 12px; width: 88px; height: 88px; border-radius: 50%;
    border: 2px solid var(--white);
    background: radial-gradient(circle at 50% 40%, #e6c9a8 0%, #c7a27c 45%, #8fa6b7 100%);
  }
  .founders-name { position: absolute; left: 125px; top: 26px; font-family: "Crimson Pro", Georgia, serif; font-weight: 600; font-size: 10.5px; }
  .founders-role { position: absolute; left: 125px; top: 42px; font-size: 5px; }
  .founders-quote { position: absolute; left: 125px; top: 57px; width: 125px; font-style: italic; font-size: 6.1px; line-height: 7.8px; }
  .honor-quote { position: absolute; left: 367px; top: 23px; width: 140px; font-style: italic; font-size: 7px; line-height: 8.9px; }
  .services { position: absolute; left: 520px; top: 24px; font-size: 5px; line-height: 8.2px; }
  .services__title { font-size: 7px; font-weight: 500; border-bottom: 0.6px solid var(--rule); width: 67px; line-height: 9px; margin-bottom: 3px; }
  .services ul { list-style: none; }
  .services li::before { content: "• "; }
  .divider { position: absolute; left: 367px; top: 74px; width: 231px; height: 0.7px; background: var(--rule); }
  .inside-logo { position: absolute; left: 367px; top: 81px; display: flex; align-items: center; gap: 3px; }
  .inside-logo .logo-mark { width: 9px; height: 9px; background: var(--white); }
  .inside-logo .logo-name { color: var(--white); font-size: 5.5px; width: 40px; }
  .rating-badge { position: absolute; left: 428px; top: 85px; width: 25px; height: 14px; border: 0.7px solid var(--white); border-radius: 1.5px; }
  .disclaimer { position: absolute; left: 463px; top: 85px; width: 135px; font-size: 3.6px; line-height: 5px; }
</style>
</head>
<body>

<section class="spread spread--outside" aria-label="Folder outside: back and front covers">
  <div class="hero-photo" role="img" aria-label="Modern Arizona living room with wide open sliding glass doors onto a pool and desert mountains"></div>
  <div class="logo-corner">
    <span class="logo-mark"></span>
    <span class="logo-name">Crestfield Pane Works</span>
  </div>
  <p class="thanks-box">Thank you for choosing Crestfield Pane Works.<br>We appreciate your trust in us to improve your home.</p>
  <h1 class="tagline">Improving Homes.<br>Improving Lives.</h1>

  <div class="outside-band">
    <div class="contact">
      <p class="contact__title">CONTACT INFORMATION:</p>
      <p>Customer Service: <strong>480.555.0187</strong></p>
      <p>Call Center: <strong>480.555.0143</strong></p>
      <p>ROC License Number: <b>#418302</b></p>
    </div>
    <div class="web web--a">
      <p>crestfieldpaneworksaz.example</p>
      <p>Follow us for the latest updates and tips.</p>
      <p class="social"><span>Chatterloop</span><span>Snapvale</span><span>ClipDrome</span><span>Rateburrow</span></p>
    </div>
    <div class="web web--b">
      <p>crestfieldpaneworksaz.example</p>
      <p>Follow us for the latest updates and tips.</p>
      <p class="social"><span>Chatterloop</span><span>Snapvale</span><span>ClipDrome</span><span>Rateburrow</span></p>
    </div>
  </div>
</section>

<section class="spread spread--inside" aria-label="Folder inside: pocket panels">
  <div class="inside-band">
    <div class="founders-photo" role="img" aria-label="Portrait of founders Doug and Marian Solvik"></div>
    <h2 class="founders-name">Doug &amp; Marian Solvik</h2>
    <p class="founders-role">Founders</p>
    <p class="founders-quote">“Our mission is to provide the best window and door solutions with a personal touch. Thank you for letting us be a part of your home improvement journey.”</p>

    <p class="honor-quote">“We’re honored to be a part of your home transformation. Our commitment to quality and customer satisfaction ensures you receive the best service and products.”</p>
    <div class="services">
      <p class="services__title">SERVICES</p>
      <ul>
        <li>Window &amp; Door Installations</li>
        <li>Window &amp; Door Replacement</li>
        <li>Energy-efficient Solutions</li>
      </ul>
    </div>
    <div class="divider"></div>
    <div class="inside-logo">
      <span class="logo-mark"></span>
      <span class="logo-name">Crestfield Pane Works</span>
    </div>
    <div class="rating-badge" aria-label="QTC A+ rating badge"></div>
    <p class="disclaimer">This business is in an industry that may require professional licensing, bonding or registration. QTC encourages you to check with the appropriate agency to be certain any requirements are currently being met.</p>
  </div>
  <svg class="pocket-notch" width="26" height="124" viewBox="0 0 26 124" aria-hidden="true">
    <polygon points="0,0 26,0 13,124" fill="#ffffff"/>
  </svg>
</section>

</body>
</html>
```